Bourbon Tasting Placemat

We are going to be hosting a Barrels and Banjos night at T&M GRILL Costilleria and we need a flyer / place mat on which to put the 5 different American Whiskeys that will be tasted. The event will be both cultural and educational in addition to culinary and musical and should have design cues that help communicate the Southern Culture, music key aspects of American Whiskey and T&M GRILL positioning as an expert in that space. Please see attached files for design cues and information to be considered in the design.

The original designs can be in English and then in the revision process we can provide the Spanish translations as all info needs to be in Spanish for the final version.

Target Market(s)

Middle to Upper class Mexicans looking to learn about American Whiskeys (bourbon, rye, moonshine, Tennessee Whiskey)

Industry/Entity Type

Event

Requirements
Must have
• Place for 5 different types of American Whiskeys (see ppt example)
Notes section
T&M GRILL branding
Cultural, educational design cues (key info, images, history, etc)

```html
<!DOCTYPE html>
<html lang="es">
<head>
<meta charset="utf-8">
<title>Barrels and Banjos night – T&amp;M GRILL Costilleria</title>
<link href="https://fonts.googleapis.com/css2?family=Oswald:wght@400;600;700&family=Roboto+Condensed:wght@400;700&family=Playfair+Display:ital,wght@1,700&display=swap" rel="stylesheet">
<style>
:root{
  --paper:#f0dfc6;
  --paper-dark:#e2c3a0;
  --ink:#5a2418;
  --rust:#9c4628;
  --text:#8a3a24;
  --tan:#d9b08e;
  --white:#fffdf9;
}
*{margin:0;padding:0;box-sizing:border-box}
html,body{width:1200px;height:900px;overflow:hidden;background:var(--paper)}
.placemat{position:relative;width:1200px;height:900px;
  background:radial-gradient(ellipse at 50% 45%,#f6e8d3 0%,var(--paper) 55%,var(--paper-dark) 100%);
  font-family:"Roboto Condensed",sans-serif;color:var(--text)}
.stripe-band{position:absolute;left:30px;right:30px;height:14px;
  border-top:2px solid var(--rust);border-bottom:2px solid var(--rust);
  background:repeating-linear-gradient(90deg,var(--rust) 0 3px,transparent 3px 9px)}
.stripe-band.top{top:8px}
.stripe-band.bottom{top:876px}
.frame{position:absolute;left:62px;top:42px;width:1078px;height:820px;border:3px solid var(--ink)}
.frame::after{content:"";position:absolute;inset:5px;border:1px solid var(--ink)}
.title-bar{position:absolute;left:272px;top:70px;width:654px;height:94px;
  border-top:3px double var(--ink);border-bottom:3px double var(--ink);
  display:flex;align-items:center;justify-content:center;gap:14px}
.title-bar .word{font-family:"Oswald",sans-serif;font-weight:700;font-size:62px;letter-spacing:1px;line-height:1;color:var(--ink)}
.title-bar .word.alt{color:var(--rust);text-shadow:3px 3px 0 var(--ink)}
.title-bar .amp{font-family:"Playfair Display",serif;font-style:italic;font-weight:700;font-size:64px;color:var(--rust);line-height:1}
.brand{position:absolute;top:78px;width:150px;text-align:center;
  font-family:"Oswald",sans-serif;font-weight:700;color:var(--ink);font-size:26px;line-height:1.05}
.brand .dot{display:block;width:14px;height:14px;border-radius:50%;background:var(--ink);margin:0 auto 6px}
.brand.left{left:96px}
.brand.right{left:955px}
.fact{position:absolute;top:203px;width:188px;height:188px;border-radius:50%;
  background:var(--white);border:6px double var(--tan);
  display:flex;flex-direction:column;align-items:center;justify-content:center;text-align:center;
  font-size:10.5px;line-height:1.3;color:var(--rust);padding:0 20px}
.fact b{color:var(--ink)}
.fact .art{display:block;border-radius:8px;background:var(--tan);margin-bottom:8px}
.fact .big{font-family:"Oswald",sans-serif;font-weight:600;font-size:19px;color:var(--ink);line-height:1.1}
.fact.photo{padding:0}
.fact.photo .art{width:168px;height:168px;border-radius:50%;margin:0;background:radial-gradient(circle,#a58468,#5e4230)}
.column{position:absolute;top:398px;width:186px;text-align:center}
.column h2{font-family:"Oswald",sans-serif;font-weight:600;font-size:21px;line-height:1.12;color:var(--ink);letter-spacing:.3px}
.column .rule{height:2px;margin:4px 20px 10px;background:var(--rust)}
.column p{font-size:7.6px;line-height:1.32;margin-bottom:8px;color:var(--text)}
.notes{position:absolute;top:703px;width:174px;height:126px;background:var(--white);
  padding:6px 8px;font-family:"Oswald",sans-serif;font-weight:600;font-size:10.5px;color:var(--ink);line-height:1.5}
.notes .line{display:inline-block;width:118px;border-bottom:1px solid var(--ink);margin-left:4px}
</style>
</head>
<body>
<main class="placemat">
  <div class="stripe-band top"></div>
  <div class="stripe-band bottom"></div>
  <div class="frame"></div>

  <div class="brand left"><span class="dot"></span>T&amp;M GRILL<br>Costilleria</div>
  <header class="title-bar">
    <span class="word">BOURBON</span><span class="amp">&amp;</span><span class="word alt">BLUEGRASS</span>
  </header>
  <div class="brand right"><span class="dot"></span>T&amp;M GRILL<br>Costilleria</div>

  <div class="fact" style="left:87px">
    <span class="art" role="img" aria-label="Mapa de Estados Unidos con estrella en Kentucky" style="width:100px;height:56px"></span>
    95% del <b>BOURBON</b> está hecho en <b>KENTUCKY</b>, pero técnicamente puede ser hecho en cualquier parte de EEUU.
  </div>
  <div class="fact" style="left:297px">
    <span class="art" role="img" aria-label="Silueta de un roble americano" style="width:96px;height:66px;border-radius:50% 50% 10px 10px"></span>
    El bourbon debe añejarse en <b>BARRICAS NUEVAS DE ROBLE AMERICANO.</b>
  </div>
  <div class="fact" style="left:506px">
    <span class="art" role="img" aria-label="Bandera de Estados Unidos ondeando" style="width:100px;height:34px"></span>
    <span class="big">EN MAYO DE 1964</span>
    el congreso de EEUU, reconoce al Bourbon como un <b>"PRODUCTO DISTINTIVO DE EEUU".</b>
  </div>
  <div class="fact" style="left:715px">
    <span class="art" role="img" aria-label="Globo terráqueo" style="width:84px;height:84px;border-radius:50%;position:absolute;top:30px;opacity:.55"></span>
    <span style="position:relative">Bourbon tiene el proceso de destilación<br><span class="big">MÁS REGULADO</span><br>del MUNDO.</span>
  </div>
  <div class="fact photo" style="left:924px">
    <span class="art" role="img" aria-label="Fotografía antigua en sepia de músicos de bluegrass tocando al aire libre"></span>
  </div>

  <section class="column" style="left:88px">
    <h2>STRAIGHT KENTUCKY<br>BOURBON</h2><div class="rule"></div>
    <p>El bourbon es una bebida destilada de la familia de los whiskeys, se caracteriza por ser ligeramente aromático y de sabor acaramelado. El bourbon whiskey, según la ley estadounidense, debe ser elaborado a base de maíz por lo menos en una concentración entre el 50% y el 70%.</p>
    <p>Otros ingredientes añadidos son: el trigo, centeno y cebada. Su periodo de envejecimiento debe ser como mínimo de dos años, no existen requerimientos legales para este periodo mínimo y que el producto final se denomine "bourbon" pero sí existen requerimientos para denominarlo straight bourbon. Por regla general el bourbon se madura durante un periodo de 5 años en barricas de roble que pueden ser nuevas y/o tostadas.</p>
    <p>El nombre de la bebida destilada proviene del lugar de Estados Unidos donde se produce de manera originaria, Bourbon County (Kentucky), que a su vez, toma su nombre de la familia real de la Casa de Borbón.</p>
  </section>
  <section class="column" style="left:298px">
    <h2>TENNESSEE<br>WHISKEY</h2><div class="rule"></div>
    <p>El Tennessee Whiskey es un straight bourbon, lo que obliga a envejecer el destilado un mínimo de 2 años dentro de la barrica. Por lo demás, las normas de producción son las mismas que las del bourbon de Kentucky con dos excepciones:</p>
    <p>La primera, que para denominarse Tennessee Whiskey sí es obligatorio que se haya producido, destilado y embotellado en el estado de Tennessee. La segunda, que antes de introducir el whiskey en la barrica para su añejamiento, éste es filtrado a través de una columna de 3 metros de carbón vegetal de madera de arce. De esta forma adquiere un aroma más suave y sabor más dulce que el bourbon de Kentucky.</p>
    <p>Los barriles de whisky se fabrican con roble blanco de América debido a que esta madera tiene la combinación necesaria de compuestos para lograr el producto final. Mientras el whisky se añeja dentro del barril, la madera se contrae y expande según los cambios climáticos que se produzcan en su entorno.</p>
  </section>
  <section class="column" style="left:507px">
    <h2>AMERICAN RYE<br>WHISKEY</h2><div class="rule"></div>
    <p>El método de destilación es prácticamente igual al del bourbon, y la gente suele confundirlos. La diferencia más notable es que el American Rye Whiskey debe ser elaborado de cebada por lo menos en un 51% de la composición total.</p>
    <p>En 1700's y 1800's el Rye Whiskey era el whiskey preferido en los estados del noroeste de los Estados Unidos, incluyendo Pensilvania y Maryland. Elias Whitcombe, un terrateniente de la época, hacía Rye Whiskey en su hacienda de Cedar Hollow.</p>
    <p>Originalmente los principales cócteles americanos como el: Old Fashioned, Manhattan y Whiskey Sours, se hacían de rye, pero con la introducción del bourbon en los estados del norte, se comenzó a cambiar el rye por el bourbon.</p>
    <p>El Rye es reconocido por sus sabores picantes y frutosos añadidos al whiskey. Mientras que el bourbon con su base mínima de 51% de maíz tiene un sabor más dulce y con más cuerpo. El rye es también mucho más seco y se puede decir que es equivalente a un Islay whiskey o whiskey escocés.</p>
  </section>
  <section class="column" style="left:716px">
    <h2>APPALACHIAN<br>MOONSHINE</h2><div class="rule"></div>
    <p>Moonshine, white lightning, mountain dew, hooch, y Tennessee white whiskey son términos para describir alcoholes de alto grado que están destilado de manera ilegal. La palabra "moonshine" proviene de la palabra "moonrakers" que fue usado para describir a los contrabandistas (que trabajaban bajo la luz de la luna) y las operaciones clandestinas usadas por las destilerías ilegales en la zona de Apalachina en el sureste de Estados Unidos.</p>
    <p>El Moonshine es muy fuerte dado el hecho de que no se corta ni se madura. Cuando sale de la destilería en su último proceso, es de color totalmente transparente y tiene entre 150 y 170 grados. Muchos dicen que en los viejos tiempos los contrabandistas lo utilizaban como gasolina y es por eso que las policías nunca los pudieron agarrar. Por otro lado el deporte de las carreras de autos creció en el sur de los EEUU por algo.</p>
  </section>
  <section class="column" style="left:925px">
    <h2>BLUEGRASS<br>MUSIC</h2><div class="rule"></div>
    <p>Bluegrass music is a form of American roots music, and a sub-genre of country music. Bluegrass was inspired by the music of Appalachia. It has mixed roots in Irish, Scottish, Welsh, and English traditional music, and also later influenced by the music of African-Americans through incorporation of Jazz elements.</p>
    <p>In bluegrass, as in some forms of Jazz, one or more instruments each takes its turn playing the melody and improvising around it, while the others perform accompaniment. This is in contrast to old-time music, in which all instruments play the melody together or one instrument carries the lead throughout while the others provide accompaniment.</p>
    <p>Bluegrass music has attracted a diverse following worldwide. Bluegrass pioneer Amos Kettridge characterized the genre as: "Scottish bagpipes and ole-time fiddlin'. It's Methodist and Holiness and Baptist. It's blues and jazz, and it has a high lonesome sound."</p>
  </section>

  <div class="notes" style="left:94px">NOMBRE<span class="line"></span><br>NOTAS:</div>
  <div class="notes" style="left:304px">NOMBRE<span class="line"></span><br>NOTAS:</div>
  <div class="notes" style="left:513px">NOMBRE<span class="line"></span><br>NOTAS:</div>
  <div class="notes" style="left:722px">NOMBRE<span class="line"></span><br>NOTAS:</div>
  <div class="notes" style="left:931px">NOMBRE<span class="line"></span><br>NOTAS:</div>
</main>
</body>
</html>
```